I need a book cover for my book titled Sunny Porch! The subtitle is Quiet Orchard Days and the the author is Marisol Dunleavy. I want the attached photo included on the cover, plus the words "I Never Met A Peach Pie I Didn't Love!" The book size is 5.06 x 7.81 in. and is 146 pages. For the color scheme, I like a chocolate brown cover with aqua blue letters. (Please note that you don't have to use these colors. Feel free to use this color scheme or whatever you colors you like!)

• Please include my photo for the back cover, along with this text:

Sunny Porch! I was tired of being tired! I was tired of acid reflux, body stiffness, and being overweight. To make matters worse, I suffered from back pain, constipation, leg pain, and lack of sleep. If you are tired of looking to medical test for your answers, this is the book for you. The key was the day I decided to make “me” a priority by being #1 on my “to-do” list.

Our healthcare system seems to be more concerned about treating illness than they are about preventing it; which is why we have so many problems with our health and wellness. That’s why I’m going to give you insights into nutrition, health care, and the pharmaceutical industry.

I’m also going to give you some insights into exercise, supplements, detoxing and essential oils; as well as what goes into your grocery cart and the foods you feed your family.

Because you’re reading this I know you’re ready to live your best life, Sunny Porch! is for you.

Here’s to a healthy you!

Here's a brief bio about the author for the back cover:

Marisol lives in Chicago with her husband, Dr. Wendell, and has three adult children. She is probably one of the most private people you will meet – BUT HAD to tell her story!

```html
<!DOCTYPE html>
<html lang="en">
<head>
<meta charset="utf-8">
<title>Sunny Porch! — Marisol Dunleavy</title>
<link rel="stylesheet" href="https://fonts.googleapis.com/css2?family=Kaushan+Script&family=Montserrat:ital,wght@0,600;0,700;1,500&display=swap">
<style>
  :root {
    --brown-deep: #3d2510;
    --brown-mid: #5a3817;
    --brown-glow: #7a4d22;
    --aqua: #4ccbc4;
    --aqua-light: #8ee6df;
    --aqua-dark: #2a9c96;
    --white: #ffffff;
  }
  html, body {
    margin: 0;
    padding: 0;
    width: 777px;
    height: 1200px;
    overflow: hidden;
    background: var(--brown-deep);
  }
  .cover {
    position: relative;
    width: 777px;
    height: 1200px;
    overflow: hidden;
    font-family: "Montserrat", sans-serif;
    color: var(--white);
  }
  .cover-pattern {
    position: absolute;
    inset: 0;
    background: radial-gradient(ellipse at 50% 48%, var(--brown-glow) 0%, var(--brown-mid) 45%, var(--brown-deep) 100%);
  }
  .series-line {
    position: absolute;
    top: 52px;
    left: 0;
    right: 0;
    text-align: center;
    font-weight: 700;
    font-size: 25px;
    letter-spacing: 0.34em;
    text-indent: 0.34em;
    text-transform: uppercase;
    margin: 0;
  }
  .title {
    position: absolute;
    left: 0;
    right: 0;
    top: 255px;
    margin: 0;
    text-align: center;
    font-family: "Kaushan Script", cursive;
    font-weight: 400;
    color: var(--aqua);
    line-height: 1;
    transform: rotate(-6deg);
  }
  .title span {
    display: block;
    font-size: 180px;
    background: linear-gradient(180deg, var(--aqua-light) 0%, var(--aqua) 40%, var(--aqua-dark) 100%);
    -webkit-background-clip: text;
    background-clip: text;
    color: transparent;
    filter: drop-shadow(4px 6px 5px rgba(0,0,0,0.45));
  }
  .title .title-line-two {
    margin-top: 45px;
    margin-left: 20px;
  }
  .ribbon {
    position: absolute;
    left: 55px;
    top: 855px;
    width: 667px;
    height: 66px;
  }
  .ribbon-text {
    position: absolute;
    left: 55px;
    top: 855px;
    width: 667px;
    height: 66px;
    line-height: 64px;
    margin: 0;
    text-align: center;
    font-style: italic;
    font-weight: 500;
    font-size: 27px;
  }
  .author {
    position: absolute;
    left: 0;
    right: 0;
    top: 1105px;
    margin: 0;
    text-align: center;
    font-weight: 700;
    font-size: 41px;
    letter-spacing: 0.13em;
    text-indent: 0.13em;
  }
</style>
</head>
<body>
  <main class="cover">
    <div class="cover-pattern" role="img" aria-label="Repeating pattern of outlined chicken wings on chocolate brown"></div>

    <p class="series-line">Quiet Orchard Days</p>

    <h1 class="title">
      <span class="title-line-one">Sunny</span>
      <span class="title-line-two">Porch!</span>
    </h1>

    <svg class="ribbon" viewBox="0 0 667 66" aria-hidden="true">
      <polygon points="0,6 667,0 650,33 667,60 0,66 18,36" fill="#4ccbc4"/>
    </svg>
    <p class="ribbon-text">I Never Met A Peach Pie I Didn't Love!</p>

    <p class="author">Marisol Dunleavy</p>
  </main>
</body>
</html>
```